BrightVent Coil Services need a Business Card!

Need a business card designed for a new start company called BrightVent! I have attached a Zip file (Please let me know if you cannot open this file) with all logos and also a sheets that includes fonts and colors. Last, you will see the design of our vans which will help design the cards too!
The card is needing to be double sided. A place for email, name, headshot, cell #, Office #, Job Title (Head shot optional)

Target Market(s)

People who need their HVAC filters changed. Residential and Commercial

Industry/Entity Type

Hvac Filter Changing Service

Contact Information for Business Card

Website: brightventcoils.example Office phone: 555.782.3096 The card is needing to be double sided. A place for email, name, headshot, cell #, Office #, Job Title (Head shot optional)

Requirements
Must have
• Color code and fonts form attached sheets and files

```html
<!DOCTYPE html>
<html lang="en">
<head>
<meta charset="utf-8">
<title>BrightVent Business Card</title>
<link rel="stylesheet" href="https://fonts.googleapis.com/css2?family=Montserrat:wght@400;500;600&display=swap">
<style>
  :root {
    --backdrop: #3b3b3d;
    --brand-navy: #064a94;
    --brand-sky: #00a6e6;
    --card-white: #ffffff;
  }
  * { margin: 0; padding: 0; box-sizing: border-box; }
  html, body { width: 1200px; height: 1200px; overflow: hidden; }
  body {
    background: var(--backdrop);
    font-family: "Montserrat", sans-serif;
    position: relative;
  }
  .card {
    position: absolute;
    left: 250px;
    width: 700px;
    height: 400px;
    border-radius: 34px;
    overflow: hidden;
  }
  .card-front { top: 150px; background: var(--card-white); }
  .card-back { top: 650px; background: var(--brand-navy); }
  .front-shape { position: absolute; inset: 0; width: 100%; height: 100%; }

  .front-brand {
    position: absolute;
    left: 36px;
    top: 172px;
    width: 330px;
    display: flex;
    align-items: center;
    gap: 12px;
  }
  .brand-dot {
    width: 18px; height: 18px; border-radius: 50%;
    background: var(--brand-sky);
    flex: none;
  }
  .brand-name {
    font-weight: 600;
    font-size: 44px;
    color: var(--brand-navy);
    letter-spacing: 0.5px;
  }

  .contact {
    position: absolute;
    left: 440px;
    top: 112px;
    width: 245px;
    color: var(--card-white);
  }
  .contact-name {
    font-weight: 600;
    font-size: 27px;
    color: var(--brand-sky);
    line-height: 1;
  }
  .contact-role {
    font-size: 16px;
    font-weight: 400;
    letter-spacing: 0.5px;
    margin-top: 4px;
  }
  .contact-list { list-style: none; margin-top: 14px; }
  .contact-list li {
    display: flex;
    align-items: center;
    gap: 7px;
    font-size: 13.5px;
    line-height: 24px;
    white-space: nowrap;
  }
  .contact-list svg { width: 15px; height: 15px; flex: none; }

  .back-brand {
    position: absolute;
    inset: 0;
    display: flex;
    align-items: center;
    justify-content: center;
    gap: 20px;
  }
  .back-brand .brand-dot { width: 28px; height: 28px; }
  .back-brand .brand-name {
    font-size: 84px;
    color: var(--card-white);
  }
</style>
</head>
<body>
  <section class="card card-front">
    <svg class="front-shape" viewBox="0 0 700 400" preserveAspectRatio="none" aria-hidden="true">
      <path d="M290 0 C410 50 420 300 330 400 L700 400 L700 0 Z" fill="var(--brand-sky)"/>
      <path d="M300 0 C422 50 432 300 342 400" fill="none" stroke="var(--card-white)" stroke-width="5"/>
      <path d="M305 0 C428 50 438 300 348 400 L700 400 L700 0 Z" fill="var(--brand-navy)"/>
    </svg>

    <div class="front-brand">
      <span class="brand-dot"></span>
      <span class="brand-name">BrightVent</span>
    </div>

    <div class="contact">
      <p class="contact-name">FULL NAME</p>
      <p class="contact-role">POSITION</p>
      <ul class="contact-list">
        <li>
          <svg viewBox="0 0 16 16"><path d="M3 1.5l3 .5 1 3-2 1.5a9 9 0 0 0 4.5 4.5L11 9l3 1 .5 3-2 2C7 15 1 9 1 3.5z" fill="var(--brand-sky)"/></svg>
          555.782.3096
        </li>
        <li>
          <svg viewBox="0 0 16 16"><rect x="1" y="3" width="14" height="10" fill="var(--brand-sky)"/><polyline points="1,3 8,9 15,3" fill="none" stroke="var(--brand-navy)" stroke-width="1.4"/></svg>
          info@brightventcoils.example
        </li>
        <li>
          <svg viewBox="0 0 16 16" fill="none" stroke="var(--brand-sky)" stroke-width="1.3"><circle cx="8" cy="8" r="6.5"/><ellipse cx="8" cy="8" rx="3" ry="6.5"/><line x1="1.5" y1="8" x2="14.5" y2="8"/><line x1="2.5" y1="4.5" x2="13.5" y2="4.5"/><line x1="2.5" y1="11.5" x2="13.5" y2="11.5"/></svg>
          brightventcoils.example
        </li>
      </ul>
    </div>
  </section>

  <section class="card card-back">
    <div class="back-brand">
      <span class="brand-dot"></span>
      <span class="brand-name">BrightVent</span>
    </div>
  </section>
</body>
</html>
```